Website for a high end London wedding DJ company

I want a website that is fairly basic but modern. It needs to look professional and smooth. I like white and black backgrounds. I am looking for something similar to this: https://www.velvetkoi.uk - at the bottom of this page it has ravenmark reviews as well. I mainly use blorvix reviews. This would need to be included, or at least some way of showing all my 5 star reviews on the first page, to get peoples attention.
My current website is www.tamblewhistle.com
My

• A way to display my reviews. Must be modern.
• Must not look cheesy and 8

```html
<!DOCTYPE html>
<html lang="en">
<head>
<meta charset="utf-8">
<title>Tamble &amp; Whistle — Wedding DJ</title>
<link rel="stylesheet" href="https://fonts.googleapis.com/css2?family=Cormorant+Garamond:wght@600&family=Poppins:wght@500&family=Jost:wght@500&display=swap">
<style>
  :root {
    --white: #ffffff;
    --ink: #111511;
    --neon: #6fe030;
    --nav-active: #7ed63a;
    --stage-top: #1f4a1c;
    --stage-mid: #153a14;
    --stage-low: #081408;
    --stage-floor: #030603;
  }
  * { box-sizing: border-box; margin: 0; padding: 0; }
  html, body { width: 1200px; height: 600px; overflow: hidden; background: var(--stage-floor); }
  .hero {
    position: relative;
    width: 1200px;
    height: 600px;
    overflow: hidden;
  }
  .hero-backdrop {
    position: absolute;
    inset: 0;
    background:
      radial-gradient(ellipse 55% 45% at 52% 30%, rgba(90,150,70,0.55), transparent 70%),
      linear-gradient(180deg, var(--stage-top) 0%, var(--stage-mid) 35%, var(--stage-low) 70%, var(--stage-floor) 100%);
  }
  .site-header {
    position: absolute;
    top: 0; left: 0; right: 0;
    height: 80px;
  }
  .brand {
    position: absolute;
    left: 42px;
    top: 22px;
    font-family: "Cormorant Garamond", serif;
    font-weight: 600;
    font-size: 26px;
    color: var(--white);
    line-height: 1;
  }
  .main-nav {
    position: absolute;
    right: 48px;
    top: 36px;
    display: flex;
    align-items: center;
    font-family: "Poppins", sans-serif;
    font-weight: 500;
    font-size: 10px;
    color: var(--white);
    text-transform: uppercase;
    line-height: 1;
  }
  .main-nav a { color: inherit; text-decoration: none; }
  .main-nav a.is-active { color: var(--nav-active); }
  .main-nav .divider { margin: 0 14px; }
  .hero-brand {
    position: absolute;
    left: 0; right: 0;
    top: 206px;
    text-align: center;
    font-family: "Cormorant Garamond", serif;
    font-weight: 600;
    font-size: 26px;
    color: var(--white);
    line-height: 1;
  }
  .hero-title {
    position: absolute;
    left: 0; right: 0;
    top: 348px;
    text-align: center;
    font-family: "Poppins", sans-serif;
    font-weight: 500;
    font-size: 33px;
    letter-spacing: 1px;
    word-spacing: 8px;
    text-transform: uppercase;
    color: transparent;
    -webkit-text-stroke: 1.4px var(--neon);
    line-height: 1;
  }
  .hero-cta {
    position: absolute;
    left: 487px;
    top: 464px;
    width: 225px;
    height: 44px;
    display: flex;
    align-items: center;
    justify-content: center;
    background: var(--white);
    color: var(--ink);
    font-family: "Jost", sans-serif;
    font-weight: 500;
    font-size: 15px;
    letter-spacing: 2px;
    text-decoration: none;
    text-transform: uppercase;
  }
</style>
</head>
<body>
  <section class="hero">
    <div class="hero-backdrop" role="img" aria-label="Photo of a dancing crowd under green laser lights at a night event"></div>

    <header class="site-header">
      <div class="brand">Tamble &amp; Whistle</div>
      <nav class="main-nav">
        <a class="is-active" href="#">DJ</a><span class="divider">|</span>
        <a href="#">Musician</a><span class="divider">|</span>
        <a href="#">Event Production</a><span class="divider">|</span>
        <a href="#">Gallery</a><span class="divider">|</span>
        <a href="#">News</a><span class="divider">|</span>
        <a href="#">Contact</a><span class="divider">|</span>
        <a href="#">Login</a>
      </nav>
    </header>

    <div class="hero-brand">Tamble &amp; Whistle</div>
    <h1 class="hero-title">Lorem ipsum dolor sit amet</h1>
    <a class="hero-cta" href="#">Contact us</a>
  </section>
</body>
</html>
```